Guarding One's Body Using Sharp Steel Cover

Hi we are producing a self defense course entitled Guarding One's Body Using Sharp Steel: A Complete Manual For Learning The Finest And Handiest Wilderness Tool In Recorded History.

I listed this as a book cover but it will actually be a DVD set, but the book cover model works fine.

See below for design examples - I am thinking we need a cover that will appeal to military/survival type people.

Target Market(s)

survivalists, cops, preppers, gun owners, martial artists, and average people wanting to learn how to defend themselves

Industry/Entity Type

Defense

Requirements
Must have
• Title: GUARDING ONE'S BODY USING SHARP STEEL: A COMPLETE MANUAL FOR LEARNING THE FINEST AND HANDIEST WILDERNESS TOOL IN RECORDED HISTORY
Nice to have
• Please look at these sample designs from other books as a model:
• https://files.plorvexa.org/media/en/4/27/BrindelQXMP.jpg - This stye is ideal.
• Other good examples:
• https://pics2.talvorn.com/8143907_k370.jpg
• http://m.zephquill.com/titles/2719058463k/48071935.jpg
• http://img.crondelmart.com/pics/P/73Tm58QyzFr._BX_KL410_TR316,410_.jpg
• http://3.cdn.wendoplix.net/-RTyZWLMMKAQ/BNWq_hufxaT/BBBBBBBBv8G/DKNp815ZaXW/s1600/Q4710392.JPG

```html
<!DOCTYPE html>
<html lang="en">
<head>
<meta charset="utf-8">
<title>Guarding One's Body Using Sharp Steel</title>
<link rel="stylesheet" href="https://fonts.googleapis.com/css2?family=Black+Ops+One&family=Russo+One&display=swap">
<style>
  :root {
    --field-green: #2f6d2f;
    --field-green-deep: #1e4f20;
    --field-green-light: #3f7d3a;
    --stencil-white: #ffffff;
    --knife-white: #fafaf5;
    --rule-white: rgba(255,255,255,0.85);
  }
  html, body {
    margin: 0;
    padding: 0;
    width: 852px;
    height: 1200px;
    overflow: hidden;
    background: var(--field-green-deep);
  }
  .cover {
    position: relative;
    width: 852px;
    height: 1200px;
    overflow: hidden;
    background:
      radial-gradient(ellipse at 50% 40%, var(--field-green-light) 0%, var(--field-green) 45%, var(--field-green-deep) 100%);
  }
  .title-art {
    position: absolute;
    left: 0;
    top: 0;
    width: 852px;
    height: 700px;
  }
  .title-line {
    font-family: "Black Ops One", "Stardos Stencil", sans-serif;
    fill: var(--stencil-white);
    text-transform: uppercase;
  }
  .knife-silhouette {
    position: absolute;
    left: 64px;
    top: 698px;
    width: 724px;
    height: 126px;
    border-radius: 60px 12px 40px 60px;
    background: linear-gradient(90deg, var(--knife-white), #e9ece4);
  }
  .subtitle {
    position: absolute;
    left: 0;
    width: 852px;
    top: 928px;
    margin: 0;
    text-align: center;
    font-family: "Russo One", sans-serif;
    font-weight: 400;
    font-size: 33px;
    line-height: 48px;
    letter-spacing: 0.5px;
    color: var(--stencil-white);
    text-transform: uppercase;
  }
  .format-mark {
    position: absolute;
    left: 68px;
    top: 1098px;
    display: flex;
    align-items: center;
    font-family: "Russo One", sans-serif;
    color: var(--stencil-white);
  }
  .format-name {
    font-size: 17px;
    padding-right: 10px;
  }
  .format-divider {
    width: 1px;
    height: 38px;
    background: var(--rule-white);
    margin-right: 10px;
  }
  .format-spec {
    font-family: Arial, Helvetica, sans-serif;
    font-size: 12px;
  }
</style>
</head>
<body>
  <main class="cover">
    <svg class="title-art" viewBox="0 0 852 700" aria-label="Guarding One's Body Using Sharp Steel">
      <text class="title-line" x="64" y="176" font-size="183" textLength="724" lengthAdjust="spacingAndGlyphs">Guarding</text>
      <text class="title-line" x="64" y="336" font-size="195" textLength="724" lengthAdjust="spacingAndGlyphs">One's Body</text>
      <text class="title-line" x="64" y="472" font-size="160" textLength="724" lengthAdjust="spacingAndGlyphs">Using Sharp</text>
      <text class="title-line" x="64" y="676" font-size="255" textLength="724" lengthAdjust="spacingAndGlyphs">Steel</text>
    </svg>

    <div class="knife-silhouette" role="img" aria-label="White silhouette of a serrated combat knife lying horizontally"></div>

    <p class="subtitle">A Complete Manual For Learning<br>The Finest And Handiest Wilderness<br>Tool In Recorded History</p>

    <div class="format-mark">
      <span class="format-name">Discora</span>
      <span class="format-divider"></span>
      <span class="format-spec">32 and 64 Bit</span>
    </div>
  </main>
</body>
</html>
```